Flyer Required for Economics Tuition business in Singapore

Require a 4-page, A4 bi-fold full colour flyer. To use attractive & vibrant colours. Can make use of colour schemes and design layouts from upcoming website revamp: http://lessonbrightpath.com/Website/
Target audience for the flyer will be 17 - 18 years old A Level students in Singapore studying in Junior Colleges.
I have attached the detailed design brief with the content required for the flyer as a file titled "Design Brief.docx" & also the logo for our business to be used in the flyer & optional photos that can be used in the flyer
Reason: Require more designs. Current designs provided are too "template" like

```html
<!DOCTYPE html>
<html lang="en">
<head>
<meta charset="utf-8">
<title>LessonBrightPath Economics Tuition – Bi-fold Flyer</title>
<link rel="stylesheet" href="https://fonts.googleapis.com/css2?family=Open+Sans:wght@400;600;700&family=PT+Serif:wght@700&display=swap">
<style>
  :root {
    --backdrop: #e9e6e1;
    --orange: #f7941d;
    --orange-deep: #e8861a;
    --blue: #0b66a8;
    --sky: #3a9ad9;
    --pink: #e9417b;
    --green: #9ac23c;
    --gold: #e3b21c;
    --white: #ffffff;
    --photo-warm: #b9825a;
    --photo-light: #d9c9b4;
  }
  * { box-sizing: border-box; margin: 0; padding: 0; }
  html, body { width: 1200px; height: 1000px; overflow: hidden; }
  body {
    background: var(--backdrop);
    font-family: "Open Sans", Arial, sans-serif;
    color: var(--white);
    position: relative;
  }
  .page {
    position: absolute;
    top: 100px;
    width: 566px;
    height: 800px;
    overflow: hidden;
    box-shadow: 0 6px 20px rgba(0,0,0,.25);
  }
  .page--back { left: 34px; background: var(--orange); }
  .page--front { left: 600px; background: var(--orange); }
  .page svg.shapes { position: absolute; inset: 0; }
  .abs { position: absolute; }

  /* Back page – About us */
  .about {
    position: absolute; left: 40px; top: 70px; width: 400px; height: 640px;
    background: var(--blue);
    border-left: 4px solid var(--gold);
    border-bottom: 4px solid var(--gold);
    padding: 24px 30px;
  }
  .about__title {
    font-family: "PT Serif", Georgia, serif; font-size: 30px; font-weight: 700;
    text-align: center; margin-bottom: 18px;
  }
  .about__heading { font-weight: 700; font-size: 14px; margin-top: 14px; }
  .about__text { font-size: 13px; line-height: 1.45; }
  .back-strip { position: absolute; left: 0; bottom: 0; width: 566px; height: 30px; background: var(--orange-deep); border-top: 3px solid var(--gold); }

  /* Front page */
  .schedule-title {
    left: 326px; top: 276px; font-family: "PT Serif", Georgia, serif;
    font-weight: 700; font-size: 21px;
  }
  .schedule-main { left: 18px; top: 340px; font-size: 12.5px; line-height: 14.2px; }
  .schedule-side { left: 318px; top: 352px; font-size: 8.5px; line-height: 10.6px; }
  .schedule-side strong { font-weight: 700; font-size: 9.5px; }
  .schedule-note { left: 260px; top: 494px; font-size: 9px; }
  .locations { left: 250px; top: 514px; width: 300px; font-size: 9.5px; line-height: 12px; }
  .locations__title { font-weight: 700; font-size: 11px; margin-bottom: 6px; }
  .locations p { margin-bottom: 7px; }
  .fees { left: 250px; top: 714px; font-family: "PT Serif", Georgia, serif; font-weight: 700; font-size: 11px; line-height: 13px; }
  .fees__title { color: var(--pink); font-size: 13px; }
  .contact-tab {
    right: 8px; top: 670px; color: var(--pink);
    font-family: "PT Serif", Georgia, serif; font-weight: 700; font-size: 10px;
    line-height: 14px; text-align: right;
  }
</style>
</head>
<body>

<!-- Inside panel: About us -->
<section class="page page--back" aria-label="About us panel">
  <div class="about">
    <h2 class="about__title">About us</h2>
    <h3 class="about__heading">Background</h3>
    <p class="about__text">Mr Daniel Lim is the Principal Tutor of Economics at LessonBrightPath Education Centre &amp; The Economics Studio.</p>
    <h3 class="about__heading">Academic Qualifications</h3>
    <p class="about__text">Mr Lim loves and specialises in Economics. He holds a Bachelor of Arts in Economics from Harbourview University (HVU). He is also currently with Lakeside Management University to pursue further studies in the subject.</p>
    <h3 class="about__heading">Teaching Experience</h3>
    <p class="about__text">Mr Lim has established a strong base of Economics at LessonBrightPath, teaching 150–200 students on average annually. Their classes and level results mean more than a thousand intensive Economics tuition hours.</p>
    <h3 class="about__heading">Style of Teaching</h3>
    <p class="about__text">Mr Lim is different from most tutors. He uses strategies to help the student excel in a subject, and tries to make clear why it matters. He engineers the methods to the appropriate right amount of practice on the quality of the lessons, aimed at real-world problems and essential application skills for the A Levels.</p>
  </div>
  <div class="back-strip"></div>
</section>

<!-- Front panel -->
<section class="page page--front" aria-label="Front panel">
  <svg class="shapes" viewBox="0 0 566 800" width="566" height="800">
    <defs>
      <linearGradient id="hallTone" x1="0" y1="0" x2="1" y2="1">
        <stop offset="0" stop-color="#d9c9b4"/>
        <stop offset=".55" stop-color="#b9825a"/>
        <stop offset="1" stop-color="#8a4a2a"/>
      </linearGradient>
      <linearGradient id="groupTone" x1="0" y1="0" x2="0" y2="1">
        <stop offset="0" stop-color="#d8d4cf"/>
        <stop offset="1" stop-color="#9c8f86"/>
      </linearGradient>
    </defs>
    <rect width="566" height="800" fill="var(--orange)"/>
    <polygon role="img" aria-label="Photo of students seated in a lecture hall writing notes"
      points="0,0 450,0 478,232 250,330 0,300" fill="url(#hallTone)"/>
    <polygon points="300,318 486,232 530,304" fill="var(--sky)"/>
    <polygon points="0,300 250,330 566,290 566,480 0,525" fill="var(--pink)"/>
    <polygon role="img" aria-label="Group photo of the tutor with his students"
      points="0,612 232,590 232,800 0,800" fill="url(#groupTone)"/>
    <polygon points="232,690 566,650 566,715 232,770" fill="var(--green)"/>
    <polygon points="378,674 566,660 566,704 378,714" fill="var(--white)"/>
    <polygon points="232,770 566,715 566,740 232,800" fill="var(--orange-deep)"/>
    <polygon points="380,800 566,745 566,800" fill="var(--blue)"/>
    <polygon points="0,606 232,584 232,590 0,612" fill="var(--gold)"/>
  </svg>

  <h2 class="abs schedule-title">Class Schedule*</h2>

  <div class="abs schedule-main">
    JC2 Monday 5pm – Jurong West<br>
    JC1 Monday 7pm – Jurong West<br>
    JC2 Tuesday 530pm – Clementi<br>
    JC1 Tuesday 730pm – Clementi<br>
    JC1 Wednesday 6pm – Bedok<br>
    JC2 Wednesday 8pm – Bedok #<br>
    JC2 Thursday 530pm – Choa Chu Kang<br>
    JC1 Thursday 730pm – Choa Chu Kang<br>
    JC2 Saturday 10am – Choa Chu Kang<br>
    JC2 Saturday 12pm – Choa Chu Kang
  </div>

  <div class="abs schedule-side">
    JC1 Saturday 2pm – Choa Chu Kang<br>
    JC2 Saturday 4pm – Choa Chu Kang<br>
    JC2 Sunday 10am – Choa Chu Kang<br>
    JC2 Sunday 12pm – Choa Chu Kang<br>
    JC1 Sunday 2pm – Choa Chu Kang<br>
    JC1 Sunday 4pm – Choa Chu Kang<br>
    <strong>call/SMS/Whatsapp us at 80001234</strong><br>
    to confirm available timings.
  </div>

  <p class="abs schedule-note">*MOST Classes are already full, call/SMS/Whatsapp us to confirm.</p>

  <div class="abs locations">
    <h3 class="locations__title">Our Locations</h3>
    <p>Choa Chu Kang: Blk 118 Maple Grove Ave 2 #01-220, S(680118)<br>2 minutes walk from CCK MRT</p>
    <p>Clementi: Blk 240 Cedar Walk #01-115, S(120240)<br>5 min bus ride from Clementi MRT</p>
    <p>Bedok: Blk 309 Birch Lane 3 #02-41 (2nd storey), S(460309)<br>7 minutes walk from Bedok MRT</p>
    <p>Jurong West: Willow Park Drive / along Lakeside West Road<br>5 minutes bus ride from JCP</p>
  </div>

  <div class="abs fees">
    <div class="fees__title">Fees &amp; Promotions</div>
    $295 per month – JC2s<br>
    $260 per month – JC1s (early bird promotion)<br>
    Sign up with a friend(s) to enjoy $20 off monthly fees.
  </div>

  <div class="abs contact-tab">
    Sign up now | Contact Us<br>
    Text/Call/Whatsapp us at 80001234
  </div>
</section>

</body>
</html>
```